Tamworth Logistics

Create a modern, simple, Elegant business card design for my business.

Services: Vexa Trucks, Transport, Contract Logistics,

Business

Include all details same as old card plus new website address: www.tamworthlogistics-demo.com.au

• Similar colors to Logo.

```html
<!DOCTYPE html>
<html lang="en">
<head>
<meta charset="utf-8">
<title>Tamworth Logistics – Business Card</title>
<link rel="stylesheet" href="https://fonts.googleapis.com/css2?family=Source+Sans+3:wght@400;600;700&display=swap">
<style>
  :root {
    --page-bg: #ecebe8;
    --card-white: #ffffff;
    --brand-blue: #1a84c9;
    --blue-light: #0ea3e4;
    --blue-mid: #0a7cc4;
    --blue-deep: #0b5590;
    --band-grey: #8e9093;
    --band-grey-dark: #5f6164;
    --text-white: #ffffff;
    --shadow: rgba(0, 0, 0, 0.22);
  }
  * { box-sizing: border-box; margin: 0; padding: 0; }
  html, body {
    width: 1200px; height: 900px; overflow: hidden;
    background: var(--page-bg);
    font-family: "Source Sans 3", "Myriad Pro", Arial, sans-serif;
  }
  .canvas { position: relative; width: 1200px; height: 900px; }

  .card {
    position: absolute;
    height: 343px;
    box-shadow: 0 6px 18px var(--shadow);
    overflow: hidden;
  }

  /* Front card */
  .card-front { left: 238px; top: 62px; width: 555px; background: var(--card-white); }
  .card-front .card-bg { position: absolute; inset: 0; }
  .brand {
    position: absolute; display: flex; align-items: center; gap: 12px;
    font-weight: 700; letter-spacing: 0.5px;
  }
  .card-front .brand {
    left: 0; right: 0; top: 58px; justify-content: center;
    color: var(--brand-blue); font-size: 38px;
  }
  .brand-dot { width: 16px; height: 16px; border-radius: 50%; background: currentColor; flex: none; }

  .person { position: absolute; left: 37px; top: 238px; color: var(--text-white); }
  .person-name { font-size: 19px; font-weight: 700; line-height: 1.2; }
  .person-title { font-size: 15px; line-height: 1.3; }

  .contact {
    position: absolute; right: 22px; top: 200px;
    color: var(--text-white); font-size: 15px; text-align: right; line-height: 20.5px;
  }
  .contact-line { display: flex; justify-content: flex-end; align-items: center; gap: 8px; }
  .contact-icon { width: 12px; height: 12px; flex: none; }
  .address { margin-top: 11px; padding-right: 20px; }

  /* Back card */
  .card-back {
    left: 459px; top: 518px; width: 560px;
    background: linear-gradient(180deg, var(--blue-light) 0%, var(--blue-mid) 50%, var(--blue-deep) 100%);
  }
  .card-back .brand {
    left: 0; right: 0; top: 98px; justify-content: center;
    color: var(--text-white); font-size: 42px;
  }
  .services {
    position: absolute; left: 0; right: 0; top: 235px;
    display: flex; justify-content: center; gap: 14px;
    color: var(--text-white); font-size: 20px;
  }
  .services li { list-style: none; }
  .services li::before { content: "\2022"; margin-right: 5px; }
</style>
</head>
<body>
<main class="canvas">

  <section class="card card-front" aria-label="Business card front">
    <svg class="card-bg" width="555" height="343" viewBox="0 0 555 343" aria-hidden="true">
      <defs>
        <linearGradient id="frontBlue" x1="0" y1="0" x2="1" y2="0">
          <stop offset="0" stop-color="#12a6e6"/>
          <stop offset="0.55" stop-color="#0b86cc"/>
          <stop offset="1" stop-color="#0b5a94"/>
        </linearGradient>
        <linearGradient id="frontGrey" x1="0" y1="0" x2="1" y2="0">
          <stop offset="0" stop-color="#a4a6a8"/>
          <stop offset="1" stop-color="#5f6164"/>
        </linearGradient>
      </defs>
      <rect x="0" y="168" width="555" height="175" fill="url(#frontGrey)"/>
      <path d="M0 205 Q 260 172 555 174 L555 343 L0 343 Z" fill="url(#frontBlue)"/>
    </svg>

    <div class="brand"><span class="brand-dot"></span>Tamworth Logistics</div>

    <div class="person">
      <p class="person-name">Daniel Harper</p>
      <p class="person-title">Managing Director</p>
    </div>

    <div class="contact">
      <p class="contact-line">044-555 010 203
        <svg class="contact-icon" viewBox="0 0 12 12" aria-hidden="true"><path d="M2.5 1 L4.5 1 L5 3.5 L3.8 4.4 Q4.8 6.8 7.6 8.2 L8.5 7 L11 7.5 L11 9.5 Q10.5 11 9 11 Q4 10.5 1 3 Q1 1.5 2.5 1 Z" fill="#fff"/></svg>
      </p>
      <p class="contact-line">info@tamworthmail-demo.com
        <svg class="contact-icon" viewBox="0 0 12 12" aria-hidden="true"><rect x="1" y="3" width="10" height="7" fill="#fff"/><path d="M1 3 L6 7 L11 3" stroke="#0b86cc" stroke-width="1" fill="none"/></svg>
      </p>
      <p class="contact-line">www.tamworthlogistics-demo.com.au
        <svg class="contact-icon" viewBox="0 0 12 12" aria-hidden="true"><circle cx="6" cy="6" r="5" fill="#fff"/><path d="M6 1 Q3 6 6 11 M6 1 Q9 6 6 11 M1 6 H11" stroke="#0b80c6" stroke-width="0.8" fill="none"/></svg>
      </p>
      <p class="address">12345, Address Goes Here<br>Country Name, 123456.</p>
    </div>
  </section>

  <section class="card card-back" aria-label="Business card back">
    <div class="brand"><span class="brand-dot"></span>Tamworth Logistics</div>
    <ul class="services">
      <li>Vexa Trucks</li>
      <li>Transport</li>
      <li>Contract Logistics</li>
    </ul>
  </section>

</main>
</body>
</html>
```